Birchford Realty Business Card

Business Card:

Somewhere on front of card, please include Broker License Number: 5839162

Website is BirchfordRealty.example

Address is:
7218 Crestover Ave E
Ashbury Falls, OH 48271

I'll let you use creative freedom on the rest; we obviously need Name, Title, Email (@BirchfordRealty.example), Office Phone, Cell Phone.

Don't want any special die-cutting, just a standard size business card.

On the back, include a place for the date and time of an appointment to be written in pen.

Requirements
Must have
• Our logo, attached to email.

```html
<!DOCTYPE html>
<html lang="en">
<head>
<meta charset="utf-8">
<title>Birchford Realty Business Card</title>
<link rel="stylesheet" href="https://fonts.googleapis.com/css2?family=Open+Sans:wght@400;600;700&display=swap">
<style>
  :root {
    --navy: #2f2f80;
    --navy-deep: #23236a;
    --grey: #8e8e93;
    --ink: #4a4a52;
    --paper: #ffffff;
    --stage: #ebe8e3;
  }
  * { box-sizing: border-box; margin: 0; padding: 0; }
  html, body { width: 1200px; height: 1023px; overflow: hidden; }
  body {
    background: var(--stage);
    font-family: "Open Sans", Arial, sans-serif;
    position: relative;
  }
  .card {
    position: absolute;
    width: 640px;
    height: 366px;
    border-radius: 4px;
    box-shadow: 0 10px 28px rgba(0,0,0,.18);
    overflow: hidden;
  }
  /* Front */
  .card-front { left: 40px; top: 60px; background: linear-gradient(135deg, #fff 40%, #f1f1f3); }
  .brand { position: absolute; display: flex; align-items: center; gap: 12px; }
  .brand-mark { width: 16px; height: 16px; background: var(--navy); flex: none; }
  .brand-name { font-weight: 700; font-size: 40px; color: var(--navy); letter-spacing: -0.5px; white-space: nowrap; line-height: 1.2; }
  .card-front .brand { left: 44px; top: 120px; }
  .agent { position: absolute; right: 40px; top: 36px; text-align: right; }
  .agent-name { font-weight: 700; font-size: 24px; color: var(--navy); }
  .agent-title { font-size: 14px; color: var(--ink); }
  .agent-license { font-size: 14px; color: var(--ink); }
  .contact { position: absolute; left: 44px; top: 210px; color: var(--ink); font-size: 15px; line-height: 1.35; }
  .address { margin-bottom: 6px; }
  .contact-list { list-style: none; }
  .contact-list li { display: flex; align-items: center; gap: 8px; }
  .contact-list svg { width: 14px; height: 14px; flex: none; }
  .contact-web { font-size: 17px; }
  /* Back */
  .card-back { left: 520px; top: 600px; background: linear-gradient(160deg, #4a4a98 0%, var(--navy) 45%, var(--navy-deep) 100%); }
  .appointment {
    position: absolute; left: 0; top: 0; width: 100%; height: 120px;
    background: var(--paper); color: var(--navy);
    font-size: 14px; font-weight: 600; letter-spacing: .5px;
  }
  .field { position: absolute; display: flex; align-items: flex-end; gap: 6px; }
  .field-line { border-bottom: 2px dotted var(--navy); height: 14px; }
  .field-date { left: 24px; top: 20px; }
  .field-date .field-line { width: 520px; }
  .field-time { left: 220px; top: 78px; }
  .field-time .field-line { width: 230px; }
  .ampm { display: inline-flex; align-items: center; gap: 5px; margin-left: 10px; }
  .box { width: 13px; height: 13px; border: 2px solid var(--navy); border-radius: 2px; }
  .tab {
    position: absolute; left: 24px; top: 64px;
    background: var(--paper); color: var(--navy);
    border: 2px solid var(--navy); border-radius: 6px;
    padding: 6px 14px; font-size: 14px; font-weight: 600; letter-spacing: .5px;
  }
  .card-back .brand { left: 0; right: 0; top: 200px; justify-content: center; }
  .card-back .brand-mark { background: #fff; }
  .card-back .brand-name { color: #fff; font-size: 46px; }
</style>
</head>
<body>
  <section class="card card-front" aria-label="Business card front">
    <div class="brand">
      <span class="brand-mark"></span>
      <span class="brand-name">Birchford Realty</span>
    </div>
    <div class="agent">
      <p class="agent-name">Dana Whitlow</p>
      <p class="agent-title">President</p>
      <p class="agent-license">License Number: 5839162</p>
    </div>
    <div class="contact">
      <p class="address">7218 Crestover Ave E<br>Ashbury Falls, OH 48271</p>
      <ul class="contact-list">
        <li><svg viewBox="0 0 14 14"><rect x="0.5" y="0.5" width="13" height="13" rx="2" fill="#2f2f80"/><path d="M4 3.5c.6 2.8 2.8 5.6 6.5 7l1-1.5-2-1-1 .8c-1-.5-2-1.6-2.5-2.6l.8-1-1-2z" fill="#fff"/></svg>555-214-7380</li>
        <li><svg viewBox="0 0 14 14"><rect x="3.5" y="0.5" width="7" height="13" rx="1.5" fill="none" stroke="#2f2f80" stroke-width="1.3"/><circle cx="7" cy="11.3" r=".8" fill="#2f2f80"/></svg>555-316-9042</li>
        <li><svg viewBox="0 0 14 14"><rect x="0.5" y="2.5" width="13" height="9" rx="1" fill="#2f2f80"/><path d="M1 3l6 5 6-5" fill="none" stroke="#fff" stroke-width="1.2"/></svg>dana@BirchfordRealty.example</li>
        <li class="contact-web"><svg viewBox="0 0 14 14"><circle cx="7" cy="7" r="6" fill="none" stroke="#2f2f80" stroke-width="1.3"/><path d="M1 7h12M7 1c-2.5 3-2.5 9 0 12M7 1c2.5 3 2.5 9 0 12" fill="none" stroke="#2f2f80" stroke-width="1"/></svg>BirchfordRealty.example</li>
      </ul>
    </div>
  </section>

  <section class="card card-back" aria-label="Business card back">
    <div class="appointment">
      <div class="field field-date"><span>DATE:</span><span class="field-line"></span></div>
      <div class="tab">NEXT APPOINTMENT</div>
      <div class="field field-time">
        <span>TIME:</span><span class="field-line"></span>
        <span class="ampm">AM <span class="box"></span></span>
        <span class="ampm">PM <span class="box"></span></span>
      </div>
    </div>
    <div class="brand">
      <span class="brand-mark"></span>
      <span class="brand-name">Birchford Realty</span>
    </div>
  </section>
</body>
</html>
```